Need posters that inspire entrepreneurs

I want to create beautiful, inspiring wall art. I'm looking for a designer to create an awesome sample (note this sample is not for real use). The winning design will form the foundation of our art "style" so there will be LOTS of ongoing work for the winning designer.

It's your challenge to create a style that is clean, inspiring and timeless, and possibly can be adapted to different colour palettes.

Looking for a perfect execution of words, image and design.

The attached example shows one idea. It should serve as an idea only.

Format of the images should be either rectangular or square. Exact size is preferably UK A4 (US letter) or max A3. Assume that a display would consist of a 4 x 4 image grid so size needs to allow for that in a small to medium size office.

The quotes I want in the 3 samples (each in an individual poster - not combined in 1 poster). Each quote should have it's own, the reason for three is to prove the design work on more than one quote. The quotes are:

1) Failure is the condiment that gives success its flavor.
– Dorian Welsby

2) Whether you think you can or think you can’t, you’re right.
– Oswald Pike

3) Ever tried. Ever failed. No matter. Try Again. Fail again. Fail better.
– Lionel Marwick

Each design should include the image of the person and the quote + any design elements you consider relevant. You should find relevant images of the individuals being quoted. The final images will not be published or used commercially in any way.

Font styles to use
Serif
Sans Serif

Colors

Designer to choose colors to be used in the design.

Requirements
Must have
• Words and headshot image - 1 per poster design.
• Please consider in the design that there will not always be photographs of the person quoted and as such the design will need to hold, whether the source is a photo, sketch or something else.
Nice to have
• None, but note that the final image will be printed on a wall mounted board, printed to the edge but not on the edge. The board will have black or white edges so consider in the design.
Should not have
• None

```html
<!DOCTYPE html>
<html lang="en">
<head>
<meta charset="utf-8">
<title>Whether you think you can – Oswald Pike</title>
<link rel="stylesheet" href="https://fonts.googleapis.com/css2?family=Bodoni+Moda:wght@400;500&display=swap">
<style>
  :root {
    --ink: #0a0c0e;
    --cyan: #18c8e8;
    --cyan-deep: #0f8aa3;
    --cyan-shadow: #0b5f72;
    --paper: #ffffff;
    --mark: #5b5b5b;
  }
  html, body {
    margin: 0;
    padding: 0;
    width: 1200px;
    height: 848px;
    overflow: hidden;
    background: var(--ink);
  }
  .poster {
    position: relative;
    width: 1200px;
    height: 848px;
    overflow: hidden;
    background: var(--ink);
    font-family: "Bodoni Moda", "Didot", serif;
  }
  .poster__art {
    position: absolute;
    inset: 0;
    width: 1200px;
    height: 848px;
  }
  .quote-mark {
    position: absolute;
    color: var(--mark);
    font-size: 330px;
    line-height: 1;
    font-weight: 500;
    opacity: 0.85;
  }
  .quote-mark--open { left: 150px; top: 475px; }
  .quote-mark--close { left: 1010px; top: 690px; }
  .quote {
    position: absolute;
    left: 342px;
    top: 538px;
    margin: 0;
    color: var(--paper);
    font-size: 60px;
    font-weight: 400;
    line-height: 82px;
    letter-spacing: 0.2px;
  }
  .quote__accent { color: var(--cyan); }
  .quote__line { display: block; white-space: nowrap; }
  .attribution {
    position: absolute;
    right: 210px;
    top: 790px;
    margin: 0;
    color: var(--paper);
    font-size: 20px;
    letter-spacing: 0.5px;
  }
</style>
</head>
<body>
<main class="poster">
  <svg class="poster__art" viewBox="0 0 1200 848" aria-hidden="false">
    <defs>
      <linearGradient id="portrait-tone" x1="0" y1="0" x2="0" y2="1">
        <stop offset="0" stop-color="var(--cyan-deep)"/>
        <stop offset="1" stop-color="var(--cyan-shadow)"/>
      </linearGradient>
    </defs>
    <polygon class="band band--cyan" points="0,0 1183,0 0,677" fill="var(--cyan)"/>
    <rect class="portrait" role="img" aria-label="Headshot portrait of Oswald Pike, cyan toned"
          x="85" y="0" width="510" height="630" rx="160" ry="160" fill="url(#portrait-tone)" opacity="0.85"/>
    <polygon class="band band--stripe" points="0,292 510,0 573,0 0,328" fill="var(--ink)"/>
    <polygon class="band band--stripe" points="0,360 629,0 672,0 0,385" fill="var(--ink)"/>
    <polygon class="band band--shade" points="0,677 1183,0 1200,0 1200,848 0,848" fill="var(--ink)"/>
  </svg>

  <span class="quote-mark quote-mark--open" aria-hidden="true">&ldquo;</span>
  <span class="quote-mark quote-mark--close" aria-hidden="true">&rdquo;</span>

  <blockquote class="quote">
    <span class="quote__line">Whether you <span class="quote__accent">think</span></span>
    <span class="quote__line"><span class="quote__accent">you can</span> or think</span>
    <span class="quote__line">you can&rsquo;t, <span class="quote__accent">you&rsquo;re right.</span></span>
  </blockquote>
  <p class="attribution">- Oswald Pike</p>
</main>
</body>
</html>
```